Ferncrest Dental, LLC business card project

Business card to be designed with current logo.
Dental office- please keep design of card that looks clean and professional.
Please include the following info:
Ferncrest Dental, LLC
Dr. Lorna Pettigrew
2871 Marlowe Street
Bethlehem, PA 18093
610-555-0193
ferncrestdental.office@examplemail.test
Hello everyone-
Reason: Just got back from overseas- will look at all designs and provide feedback. Thank you!
Reason: Polling my friends for the final selection-
thank you to all those that participated- so many talented designers!

```html
<!DOCTYPE html>
<html lang="en">
<head>
<meta charset="utf-8">
<title>Ferncrest Dental, LLC – Business Card</title>
<link rel="stylesheet" href="https://fonts.googleapis.com/css2?family=Open+Sans:wght@400;600;700&display=swap">
<style>
  :root {
    --bg: #e9ebe6;
    --green-light: #a8d631;
    --green-mid: #8cc51e;
    --green-dark: #5f9e12;
    --green-text: #6aa51c;
    --white: #ffffff;
    --paper-edge: #e4e4e4;
    --ink: #333333;
    --ink-soft: #444444;
  }
  * { margin: 0; padding: 0; box-sizing: border-box; }
  html, body {
    width: 1200px; height: 951px; overflow: hidden;
    background: var(--bg);
    font-family: "Open Sans", Arial, sans-serif;
  }
  .canvas { position: relative; width: 1200px; height: 951px; }

  .card {
    position: absolute;
    width: 700px; height: 400px;
    border-radius: 24px;
    overflow: hidden;
    box-shadow: 0 10px 28px rgba(0,0,0,0.18);
  }

  /* Front */
  .card-front {
    left: 90px; top: 60px;
    background: radial-gradient(ellipse at 35% 30%, var(--green-light) 0%, var(--green-mid) 55%, var(--green-dark) 100%);
  }
  .front-brand {
    position: absolute; left: 90px; top: 170px;
    display: flex; align-items: center; gap: 14px;
  }
  .brand-dot {
    width: 22px; height: 22px; border-radius: 50%;
    background: var(--white);
  }
  .brand-name {
    font-weight: 400;
    font-size: 40px;
    letter-spacing: -0.5px;
  }
  .front-brand .brand-name { color: var(--white); }

  /* Back */
  .card-back {
    left: 410px; top: 490px;
    background: linear-gradient(180deg, var(--white) 0%, #f4f4f4 70%, var(--paper-edge) 100%);
  }
  .back-brand {
    position: absolute; left: 110px; top: 40px;
    display: flex; align-items: center; gap: 14px;
  }
  .back-brand .brand-dot { background: var(--green-text); }
  .back-brand .brand-name { color: var(--green-text); font-size: 38px; }

  .doctor-name {
    position: absolute; left: 50px; top: 138px;
    font-size: 22px; font-weight: 700; color: var(--ink);
  }
  .address {
    position: absolute; left: 50px; top: 194px;
    font-style: normal; font-size: 16px; line-height: 23px; color: var(--ink-soft);
    display: flex; gap: 8px;
  }
  .contacts {
    position: absolute; left: 315px; top: 186px;
    list-style: none; font-size: 16px; line-height: 22px; color: var(--ink-soft);
  }
  .contacts li { display: flex; align-items: center; gap: 8px; white-space: nowrap; }
  .icon { width: 14px; height: 14px; flex: none; fill: var(--green-text); }
  .address .icon { margin-top: 4px; }

  .wave-band { position: absolute; left: 0; bottom: 0; width: 700px; height: 150px; }
</style>
</head>
<body>
<main class="canvas">

  <section class="card card-front" aria-label="Card front">
    <div class="front-brand">
      <span class="brand-dot"></span>
      <span class="brand-name">Ferncrest Dental, LLC</span>
    </div>
  </section>

  <section class="card card-back" aria-label="Card back">
    <div class="back-brand">
      <span class="brand-dot"></span>
      <span class="brand-name">Ferncrest Dental, LLC</span>
    </div>

    <h1 class="doctor-name">Dr. Lorna Pettigrew</h1>

    <address class="address">
      <svg class="icon" viewBox="0 0 14 14"><path d="M7 1 L13 7 H11 V13 H8.5 V9 H5.5 V13 H3 V7 H1 Z"/></svg>
      <span>2871 Marlowe Street<br>Bethlehem, PA 18093</span>
    </address>

    <ul class="contacts">
      <li>
        <svg class="icon" viewBox="0 0 14 14"><path d="M3.2 1 L5.3 3.6 L4.2 5.2 C5 7 6.6 8.8 8.6 9.8 L10.2 8.7 L13 10.8 L11.6 13 C6.6 12.6 1.4 7.4 1 2.4 Z"/></svg>
        <span>610-555-0193</span>
      </li>
      <li>
        <svg class="icon" viewBox="0 0 14 14"><path d="M1 3 H13 V11 H1 Z M1.8 3.6 L7 8 L12.2 3.6" stroke="#fff" stroke-width="0.9"/></svg>
        <span>ferncrestdental.office@examplemail.test</span>
      </li>
      <li>
        <svg class="icon" viewBox="0 0 14 14"><circle cx="7" cy="7" r="6"/></svg>
        <span>www.ferncrestdental.office@examplemail.test</span>
      </li>
    </ul>

    <svg class="wave-band" viewBox="0 0 700 150" preserveAspectRatio="none" aria-hidden="true">
      <path d="M0 40 C180 95 420 110 700 55 L700 150 L0 150 Z" fill="#c9e48a"/>
      <path d="M0 70 C200 120 440 125 700 80 L700 150 L0 150 Z" fill="var(--white)"/>
      <path d="M0 88 C220 135 460 135 700 95 L700 150 L0 150 Z" fill="var(--green-mid)"/>
      <path d="M0 118 C250 150 480 140 700 118 L700 150 L0 150 Z" fill="var(--green-dark)"/>
    </svg>
  </section>

</main>
</body>
</html>
```